Velvet Harbor for sale at the 2019 Tandor Crest Mare Auction on 30 May 2019

I am selling my broodmare at the 2019 Tandor Crest Mare auction on 30 May 2019. I need a flyer to hand out to potential buyers. I have included the required information in the attached word document. I can provide more images if required. I am thinking that a DL double sided or an A5 will suit best. I'm happy to provide more information as required.

Target Market(s)

Race horse breeders, people who buy broodmares.

Font styles to use
Serif
Sans Serif
Script

Colors

Designer to choose colors to be used in the design.

Requirements
Must have
• All of the content provided in the attached brief, however it is not necessary to have the words exactly as per the brief. The brief is for information purposes.
Nice to have
• Innovation...

```html
<!DOCTYPE html>
<html lang="en">
<head>
<meta charset="utf-8">
<title>Velvet Harbor – Flyer Design A5</title>
<link href="https://fonts.googleapis.com/css2?family=Montserrat:wght@400;800&family=Passion+One:wght@700&family=Rajdhani:wght@400;500;700&display=swap" rel="stylesheet">
<style>
  :root {
    --ink: #2a2a2a;
    --page-top: #3b3b3b;
    --page-bottom: #131313;
    --red: #c41e2f;
    --red-text: #e8404f;
    --white: #f2f2f2;
    --grey-text: #e4e4e4;
    --ring-dark: #1d1d1d;
    --turf-light: #9bc46a;
    --turf-dark: #2f6a2a;
    --sky: #c9d8e0;
  }
  * { margin: 0; padding: 0; box-sizing: border-box; }
  html, body { width: 1200px; height: 1019px; overflow: hidden; background: #fff; }
  body { position: relative; font-family: "Rajdhani", sans-serif; color: var(--grey-text); }

  .sheet-title {
    position: absolute; left: 0; top: 42px; width: 1200px; text-align: center;
    font-family: "Montserrat", sans-serif; font-weight: 800; font-size: 62px;
    color: var(--ink); letter-spacing: 1px; line-height: 1;
  }
  .sheet-subtitle {
    position: absolute; left: 0; top: 115px; width: 1200px; text-align: center;
    font-family: "Montserrat", sans-serif; font-weight: 400; font-size: 29px;
    color: var(--ink); letter-spacing: 1px;
  }

  .flyer-page {
    position: absolute; top: 190px; width: 563px; height: 799px; overflow: hidden;
    background: linear-gradient(180deg, var(--page-top) 0%, #222 45%, var(--page-bottom) 100%);
  }
  .flyer-page--front { left: 30px; }
  .flyer-page--back { left: 610px; }

  .corner-graphic { position: absolute; left: 0; top: 0; width: 563px; height: 799px; }

  .hero-photo {
    position: absolute; left: 340px; top: 24px; width: 225px; height: 188px;
    border-radius: 45% 30% 20% 45%;
    background: radial-gradient(ellipse at 45% 55%, #3a2a22 0%, #24180f 45%, rgba(36,24,15,0) 72%);
  }

  .horse-name {
    position: absolute; left: 44px; top: 36px;
    font-family: "Passion One", sans-serif; font-weight: 700; font-size: 50px; line-height: 1;
    color: var(--red); -webkit-text-stroke: 2px var(--white); paint-order: stroke fill;
    letter-spacing: 0.5px;
  }
  .pedigree {
    position: absolute; left: 0; width: 308px; top: 97px; text-align: right;
    font-size: 16px; font-weight: 500; color: var(--white);
  }
  .sale-details {
    position: absolute; left: 37px; top: 132px; width: 500px;
    font-size: 13.5px; font-weight: 500; line-height: 20px; color: var(--white);
  }
  .sale-details .label { color: var(--red-text); font-weight: 700; }
  .sale-details strong { font-weight: 700; }

  .medallion { position: absolute; width: 212px; height: 212px; }
  .medallion__crescent {
    position: absolute; width: 212px; height: 212px; border-radius: 50%; background: var(--red);
  }
  .medallion--lean-left .medallion__crescent { left: -8px; top: 8px; }
  .medallion--lean-right .medallion__crescent { left: 8px; top: 8px; }
  .medallion__photo {
    position: absolute; left: 0; top: 0; width: 212px; height: 212px; border-radius: 50%;
    border: 5px solid var(--white); box-shadow: inset 0 0 0 4px var(--ring-dark);
    background: linear-gradient(180deg, var(--sky) 0%, #6f8a6c 38%, var(--turf-light) 62%, var(--turf-dark) 100%);
  }
  .connector { position: absolute; height: 3px; width: 36px; background: var(--white); }

  .race-result { position: absolute; width: 240px; font-size: 13px; line-height: 16px; font-weight: 500; color: var(--white); }
  .race-result--right { text-align: right; }
  .race-result__headline {
    font-weight: 700; font-size: 19px; line-height: 22px; color: var(--red-text); margin-bottom: 1px;
  }
</style>
</head>
<body>
  <h1 class="sheet-title">PREVIEW</h1>
  <p class="sheet-subtitle">Flyer Design - A5 size</p>

  <!-- Front page -->
  <section class="flyer-page flyer-page--front">
    <svg class="corner-graphic" viewBox="0 0 563 799" aria-hidden="true">
      <polygon points="320,0 563,254 563,238 338,0" fill="#ffffff"/>
      <polygon points="338,0 563,0 563,238" fill="var(--red)"/>
      <polygon points="0,710 0,799 88,799" fill="var(--red)"/>
    </svg>
    <div class="hero-photo" role="img" aria-label="Photo of the mare galloping with a jockey in red silks"></div>

    <h2 class="horse-name">Velvet Harbor</h2>
    <p class="pedigree">by Brisklane, out of Carenza</p>

    <div class="sale-details">
      <p><span class="label">Lot number:</span> 1414</p>
      <p><span class="label">Stable:</span> QC 6</p>
      <p><span class="label">Sale date:</span> 30 May 2019</p>
      <p><span class="label">Sale:</span> 2019 Tandor Crest Mare Auction</p>
      <p><span class="label">Race record:</span> 7 wins, 2 seconds, 2 thirds (27-7:2:2). $205,400 prizemoney</p>
      <p>In foal to <strong>Far Meadow</strong>, sire of: Stellar Drive (winner of the Group 3 Lantern Bay Stakes by 7.5L), Hold Fast (winner of the Group 2 Wyndmoor Plate), Gale Runner (winner of the Tandor Crest Sundial Classic), Swift Arrow, Silver Comet plus more</p>
    </div>

    <div class="medallion medallion--lean-left" style="left:34px; top:330px;">
      <div class="medallion__crescent"></div>
      <div class="medallion__photo" role="img" aria-label="Race photo of the mare winning at Kestrel Park"></div>
    </div>
    <div class="connector" style="left:248px; top:434px;"></div>
    <div class="race-result" style="left:294px; top:396px;">
      <p class="race-result__headline">Velvet Harbor wins by 3.5L</p>
      <p>Class 6 Handicap – 1400m</p>
      <p>Riverton Racing Club (Kestrel Park),</p>
      <p>21 January 2017</p>
    </div>

    <div class="medallion medallion--lean-right" style="left:322px; top:534px;">
      <div class="medallion__crescent"></div>
      <div class="medallion__photo" role="img" aria-label="Race photo of the mare crossing the finish line"></div>
    </div>
    <div class="connector" style="left:282px; top:636px;"></div>
    <div class="race-result race-result--right" style="left:30px; top:604px;">
      <p class="race-result__headline">Velvet Harbor wins by 2.8L</p>
      <p>No More Than One Metro Win</p>
      <p>Handicap – 1400m</p>
      <p>Riverton Racing Club (Kestrel Park),</p>
      <p>10 December 2016</p>
    </div>
  </section>

  <!-- Back page -->
  <section class="flyer-page flyer-page--back">
    <svg class="corner-graphic" viewBox="0 0 563 799" aria-hidden="true">
      <polygon points="563,690 563,799 458,799" fill="var(--red)"/>
    </svg>

    <div class="medallion medallion--lean-left" style="left:34px; top:54px;">
      <div class="medallion__crescent"></div>
      <div class="medallion__photo" role="img" aria-label="Race photo of the mare passing the winning post at Kestrel Park"></div>
    </div>
    <div class="connector" style="left:248px; top:157px;"></div>
    <div class="race-result" style="left:294px; top:112px; width:250px;">
      <p class="race-result__headline">Velvet Harbor beats Rivoleta by 1.3L</p>
      <p>Class 6 Plate – 1300m</p>
      <p>Riverton Racing Club (Kestrel Park),</p>
      <p>29 April 2017</p>
    </div>

    <div class="medallion medallion--lean-right" style="left:318px; top:280px;">
      <div class="medallion__crescent"></div>
      <div class="medallion__photo" role="img" aria-label="Race photo of the mare winning at Ashgrove"></div>
    </div>
    <div class="connector" style="left:280px; top:384px;"></div>
    <div class="race-result race-result--right" style="left:29px; top:352px;">
      <p class="race-result__headline">Velvet Harbor wins by 2.3L</p>
      <p>Class 4 Handicap – 1400m</p>
      <p>Riverton Racing Club (Ashgrove),</p>
      <p>23 November 2016</p>
    </div>

    <div class="medallion medallion--lean-left" style="left:34px; top:506px;">
      <div class="medallion__crescent"></div>
      <div class="medallion__photo" role="img" aria-label="Race photo of the mare winning her debut at the Coral Coast"></div>
    </div>
    <div class="connector" style="left:248px; top:609px;"></div>
    <div class="race-result" style="left:294px; top:565px; width:250px;">
      <p class="race-result__headline">Velvet Harbor wins on debut at the Coral Coast!</p>
      <p>Maiden – 1000m</p>
      <p>Coral Coast Turf Club,</p>
      <p>23 October 2015</p>
    </div>
  </section>
</body>
</html>
```